Corporate Design für Veranstalter von Fundraising-Events zum Thema Naturschutz
Zielgruppe
Wir sind eine Organisation, die Fundraising Events zum Thema Naturschutz organisiert. Spenden gehen an internationale Naturschutzprojekte. Unsere Zielgruppe sind große Firmen, wie auch private Spender von jung bis alt.
Aufgabenstellung
Wir suchen ein hochwertiges Design, das auf internationaler Bühne Zuspruch findet. Unternehmenssprache ist Englisch, daher bitte jeglichen Text in englischer Sprache verfassen. Der Name unser Organisation ist Colina Brava, was grüner Schmetterling in Spanisch bedeutet. Unser Logo sollte daher einen grünen Schmetterling enthalten und die Farbe Grün (hellgrün-saftig) die dominante Farbe im Corporate Design sein. Je nach Design könnten wir uns als weitere Farbakzente erdige Töne vorstellen, vorrangig orange.

```html
<!DOCTYPE html>
<html lang="en">
<head>
<meta charset="utf-8">
<title>Colina Brava – Business Cards</title>
<link rel="stylesheet" href="https://fonts.googleapis.com/css2?family=Montserrat:wght@300;400;500&family=Roboto:wght@300;400&display=swap">
<style>
  :root {
    --backdrop: #a2a2a2;
    --paper: #ececec;
    --ink: #333333;
    --ink-soft: #8a8a8a;
    --charcoal-dark: #262626;
    --charcoal-light: #3d3d3d;
    --leaf-green: #7cb83a;
    --leaf-green-deep: #5f9a24;
    --white: #f4f4f4;
    --muted: #bdbdbd;
  }
  * { box-sizing: border-box; margin: 0; padding: 0; }
  html, body { width: 1200px; height: 900px; overflow: hidden; }
  body {
    background: var(--backdrop);
    font-family: "Montserrat", Arial, sans-serif;
    position: relative;
  }
  .card {
    position: absolute;
    width: 525px;
    height: 300px;
    overflow: hidden;
    top: 300px;
  }
  .card__band {
    position: absolute;
    left: 0; right: 0; bottom: 0;
    height: 9px;
    background: linear-gradient(90deg, var(--leaf-green-deep), var(--leaf-green));
  }

  /* Front */
  .card--front { left: 630px; background: var(--paper); }
  .front-brand {
    position: absolute;
    left: 0; right: 0; top: 70px;
    text-align: center;
  }
  .front-brand__dot {
    display: block;
    width: 54px; height: 54px;
    margin: 0 auto 22px;
    border: 3px solid var(--leaf-green);
    border-radius: 50%;
  }
  .front-brand__name {
    font-weight: 400;
    font-size: 26px;
    letter-spacing: 1.5px;
    color: var(--ink);
  }
  .front-brand__tagline {
    margin-top: 4px;
    font-weight: 300;
    font-size: 11px;
    letter-spacing: 2.2px;
    color: var(--ink-soft);
  }

  /* Back */
  .card--back {
    left: 45px;
    background: linear-gradient(160deg, var(--charcoal-light), var(--charcoal-dark));
  }
  .back-ornament {
    position: absolute;
    left: 0; top: 0;
    width: 300px; height: 291px;
    background: radial-gradient(ellipse at 40% 55%, rgba(124, 184, 58, 0.10), rgba(124, 184, 58, 0) 70%);
  }
  .back-brand {
    position: absolute;
    left: 40px; top: 118px;
    width: 220px;
    text-align: center;
  }
  .back-brand__name {
    font-weight: 400;
    font-size: 21px;
    letter-spacing: 1px;
    color: var(--leaf-green);
  }
  .back-brand__tagline {
    margin-top: 3px;
    font-weight: 300;
    font-size: 9px;
    letter-spacing: 1.8px;
    color: var(--leaf-green);
  }
  .contact {
    position: absolute;
    left: 300px; top: 58px;
    font-family: "Roboto", Arial, sans-serif;
    color: var(--muted);
  }
  .contact__name {
    font-weight: 400;
    font-size: 19px;
    letter-spacing: 3px;
    color: var(--white);
  }
  .contact__role {
    font-size: 10px;
    color: var(--leaf-green);
    margin: 3px 0 18px;
  }
  .contact__row {
    display: flex;
    align-items: flex-start;
    gap: 10px;
    font-size: 10px;
    line-height: 1.3;
    margin-bottom: 14px;
  }
  .contact__icon { flex: none; width: 10px; height: 10px; margin-top: 1px; fill: var(--leaf-green); }
</style>
</head>
<body>

  <section class="card card--back" aria-label="Business card back">
    <div class="back-ornament" role="img" aria-label="Decorative sweeping green line ornament"></div>
    <div class="back-brand">
      <div class="back-brand__name">COLINA BRAVA</div>
      <div class="back-brand__tagline">NATURE CONSERVATION</div>
    </div>
    <div class="contact">
      <div class="contact__name">FULL NAME</div>
      <div class="contact__role">Position</div>
      <div class="contact__row">
        <svg class="contact__icon" viewBox="0 0 10 10"><path d="M5 0a3.6 3.6 0 0 0-3.6 3.6C1.4 6.3 5 10 5 10s3.6-3.7 3.6-6.4A3.6 3.6 0 0 0 5 0zm0 5a1.4 1.4 0 1 1 0-2.8A1.4 1.4 0 0 1 5 5z"/></svg>
        <span>Building Street<br>City Country</span>
      </div>
      <div class="contact__row">
        <svg class="contact__icon" viewBox="0 0 10 10"><path d="M2 0.3l1.6 2.2-0.9 1.1c0.6 1.3 1.4 2.1 2.7 2.7l1.1-0.9 2.2 1.6-0.8 2c-4.3-0.3-7.6-3.6-7.9-7.9z"/></svg>
        <span>+12 345 6789<br>+12 345 6789</span>
      </div>
      <div class="contact__row">
        <svg class="contact__icon" viewBox="0 0 10 10"><path d="M0 2h10v6H0z M0 2l5 3.5L10 2" stroke="var(--charcoal-dark)" stroke-width="0.8"/></svg>
        <span>www.colinabrava-example.com<br>info@colinabrava-example.com</span>
      </div>
    </div>
    <div class="card__band"></div>
  </section>

  <section class="card card--front" aria-label="Business card front">
    <div class="front-brand">
      <span class="front-brand__dot"></span>
      <div class="front-brand__name">COLINA BRAVA</div>
      <div class="front-brand__tagline">NATURE CONSERVATION</div>
    </div>
    <div class="card__band"></div>
  </section>

</body>
</html>
```